Webpage for co-working space for tech startups

We have an established co-working space in Aalborg Denmark where we have around 30 companies sharing office space. We are starting a new chapter for us and would like to have a new graphical image - new logo and new webpage, but keep the same name. The webpage should be professional, but also "fun", not too serious. We are all about working hard on our companies, but also taking some time off in between and being social and having fun. We are not corporate, but want to project the image that we are serious about what we do.

We currently have a black/red logo (see www.pebblehive.dk or test.pebblehive.dk), but are interesting in having a new logo design, so colour can be chosen freely. Currently our logo is a big PEBBLE and a little hive underneath the PEBBLE. The new logo will be one word "pebblehive" with a small logo before or on top.

If we can make a good webpage for this project, then I have a second more simple project which is also a small single page wordpress site which I would also like to have made.

Target Market(s)

tech startups - relatively new companies, typically younger people 20-35 with a tech background - business or programming, preferably both

Industry/Entity Type

PEBBLE

Logo Text

pebblehive

Coding

Coded - Design and coding required

Number of Pages Required

4 page

Font styles to use
Sans Serif

Colors

Designer to choose colors to be used in the design.

Requirements
Must have
• Wordpress CMS.
• Mobile and PC optimized
• 2 languages - English and Danish
• Four sections, could be four pages, or four sections of a single page.
• "Home", "Residents", "Our Working Space", "Our Event Space"
• Footer of page or pages should have contact information.
• "Home" has some information about who we are and what we do
• "Residents" has a list of all our residents - it should be possible to easily add and removed new / old residents - See one example here: http://test.pebblehive.dk/en_GB/beboere/ or another example here: http://www.pebblehive.dk/beboere/ - one of our colleagues http://quillbarn.dk/startups/ or another one of our colleagues http://www.copperdeckhall.dk/residents/
• "Our working space" will have a description of our building, a map of where it is and a bunch of photos which show the different offices, meeting rooms and people working
• "Our events space" will have a description of our event spaces, details of cost + different arrangments of furniture, and lots of photos of events, see here for an example http://www.pebblehive.dk/lej-vores-lokaler/
• Our current webpage - www.pebblehive.dk was put together very quickly and has not really been optimized. We started a new webpage test.pebblehive.dk, but it was never really finished.
• We are looking for a simple webpage, not too much going on. Examples of some of our colleagues in the business http://quillbarn.dk/, http://www.copperdeckhall.dk/,
Nice to have
• http://www.copperdeckhall.dk/ is a really good template for us. If we can get something like this, we are happy.

```html
<!DOCTYPE html>
<html lang="en">
<head>
<meta charset="utf-8">
<title>PebbleHive – Our Working Space</title>
<link href="https://fonts.googleapis.com/css2?family=Signika:wght@400;600;700&family=Open+Sans:wght@400;600&family=Montserrat:wght@500;600&family=Cabin+Condensed:wght@500&display=swap" rel="stylesheet">
<style>
:root{
  --red:#b30f10;
  --red-band:#b5161a;
  --ink:#222;
  --muted:#6b6b6b;
  --light:#f1f1f1;
  --black:#0b0b0b;
  --white:#fff;
}
*{margin:0;padding:0;box-sizing:border-box}
html,body{width:826px;height:1200px;overflow:hidden;background:var(--white)}
body{position:relative;font-family:"Open Sans",sans-serif;color:var(--ink)}
.abs{position:absolute}

/* hero */
.hero{position:absolute;left:0;top:0;width:826px;height:203px;
  background:radial-gradient(ellipse at 45% 30%,#6a5a4e 0%,#3a302a 35%,#1c1815 75%)}
.hero-photo{position:absolute;inset:0}
.brand{position:absolute;left:68px;top:26px;font-family:"Montserrat",sans-serif;font-weight:600;
  font-size:15px;letter-spacing:1px;color:var(--white)}
.nav{position:absolute;left:339px;top:27px;display:flex;gap:19px;
  font-family:"Cabin Condensed",sans-serif;font-size:11.5px;color:var(--white)}
.lang{position:absolute;left:697px;top:25px;display:flex;align-items:center;gap:5px;
  font-family:"Cabin Condensed",sans-serif;font-size:11px;color:var(--white)}
.lang-chip{width:27px;height:20px;border:1px solid var(--white);background:#2a3f7a}
.hero-rule{position:absolute;left:68px;top:64px;width:690px;height:1px;background:rgba(255,255,255,.45)}
.hero-title{position:absolute;left:0;width:826px;top:118px;text-align:center;
  font-family:"Signika",sans-serif;font-weight:700;font-size:41px;letter-spacing:1.5px;color:var(--white)}

/* intro */
.section-title{position:absolute;left:0;width:826px;top:251px;text-align:center;
  font-family:"Signika",sans-serif;font-weight:700;font-size:24px;letter-spacing:.5px;color:var(--red)}
.section-rule{position:absolute;left:371px;top:292px;width:84px;height:2px;background:var(--red)}
.intro{position:absolute;left:68px;width:690px;top:320px;text-align:center;
  font-family:"Signika",sans-serif;font-size:10.4px;line-height:15.3px;color:#444}

/* cards */
.card{position:absolute;top:399px;width:219px}
.card-photo{width:219px;height:155px}
.card-title{margin-top:30px;font-family:"Signika",sans-serif;font-weight:600;font-size:17.5px;color:#1d1d1d;margin-left:-2px}
.card-rule{margin-top:5px;width:42px;height:3px;background:var(--red)}
.card-text{margin-top:12px;font-size:10.3px;line-height:18.4px;color:var(--muted);text-align:justify}
.price{margin-top:16px;display:flex;width:74px;height:30px;border:1.5px solid var(--red);padding:2px}
.price-cur{width:31px;background:var(--red);color:var(--white);font-family:"Signika",sans-serif;font-weight:700;
  font-size:12px;display:flex;align-items:center;justify-content:center}
.price-val{flex:1;color:var(--red);font-family:"Signika",sans-serif;font-weight:700;font-size:13px;
  display:flex;align-items:center;justify-content:center}

/* home band */
.home-band{position:absolute;left:0;top:794px;width:826px;height:64px;background:var(--light)}
.btn-outline{position:absolute;left:344px;top:16px;width:138px;height:34px;border:1.5px solid var(--red);
  color:var(--red);font-family:"Signika",sans-serif;font-weight:700;font-size:12px;letter-spacing:.6px;
  display:flex;align-items:center;justify-content:center}

/* contact band */
.contact{position:absolute;left:0;top:858px;width:826px;height:188px;
  background:linear-gradient(90deg,#c0181b 0%,var(--red-band) 50%,#a81216 100%);color:var(--white);
  font-family:"Montserrat",sans-serif}
.cta-head{position:absolute;left:68px;top:51px;font-size:15px;font-weight:600;line-height:23px}
.cta-btn{position:absolute;left:68px;top:109px;width:111px;height:32px;border:1.5px solid var(--white);
  font-size:11px;font-weight:600;letter-spacing:.5px;display:flex;align-items:center;justify-content:center}
.divider{position:absolute;left:340px;top:32px;width:1px;height:126px;background:rgba(255,255,255,.55)}
.col-head{position:absolute;top:48px;font-size:11.5px;font-weight:600}
.info{position:absolute;left:370px;display:flex;gap:10px;font-size:8.6px;font-weight:500;line-height:15px}
.info svg{flex:none;margin-top:3px}
.hours{position:absolute;left:609px;top:77px;font-size:8.6px;font-weight:500;line-height:15.5px}

/* footer */
.footer{position:absolute;left:0;top:1046px;width:826px;height:154px;background:var(--black);color:var(--white)}
.foot-nav{position:absolute;left:68px;top:53px;display:flex;font-family:"Cabin Condensed",sans-serif;font-size:10.8px}
.foot-nav span.sep{margin:0 14px}
.foot-rule{position:absolute;left:68px;top:76px;width:408px;height:1px;background:#555}
.copyright{position:absolute;left:68px;top:84px;font-family:"Montserrat",sans-serif;font-size:9px;font-weight:500}
.foot-brand{position:absolute;left:569px;top:47px;width:189px;text-align:right;font-family:"Montserrat",sans-serif;
  font-weight:600;font-size:18px;letter-spacing:1px}
.social{position:absolute;left:631px;top:81px;display:flex;gap:6px}
.social span{width:20px;height:20px;border-radius:50%;background:#5a5a5a}
</style>
</head>
<body>

<header class="hero">
  <div class="hero-photo" role="img" aria-label="Dimly lit office with a woman working at a desk lamp"></div>
  <div class="brand">PEBBLEHIVE</div>
  <nav class="nav"><span>Home</span><span>Residents</span><span>Our Working Space</span><span>Our Event Space</span><span>Contact</span></nav>
  <div class="lang"><span class="lang-chip"></span><span>Eng</span>
    <svg width="6" height="4" viewBox="0 0 6 4"><path d="M0 0h6L3 4z" fill="#fff"/></svg></div>
  <div class="hero-rule"></div>
  <h1 class="hero-title">OUR WORKING SPACE</h1>
</header>

<h2 class="section-title">WORKING SPACE</h2>
<div class="section-rule"></div>
<p class="intro">The corporate community at PebbleHive is a community of tech entrepreneurs with global growth ambitions. The vision is to create the best possible conditions for North Jutland entrepreneurs by offering them an environment where they can share knowledge, experience, resources, ideas, motivation and inspiration daily.</p>

<article class="card" style="left:68px">
  <div class="card-photo" role="img" aria-label="Open office with white desks and dark walls" style="background:linear-gradient(160deg,#d9dadd 0%,#6b6e74 45%,#2b2c30 100%)"></div>
  <h3 class="card-title">NAM LIBERO TEMPORE</h3>
  <div class="card-rule"></div>
  <p class="card-text">The PebbleHive office community is run by the PebbleHive fmba association, which is a voluntary association.</p>
  <div class="price"><span class="price-cur">$</span><span class="price-val">250</span></div>
</article>

<article class="card" style="left:303px">
  <div class="card-photo" role="img" aria-label="Bright office floor with large windows and workstations" style="background:linear-gradient(160deg,#f2f2f0 0%,#cfd1cf 55%,#8e918e 100%)"></div>
  <h3 class="card-title">SIMILIQUE SUNT</h3>
  <div class="card-rule"></div>
  <p class="card-text">The PebbleHive office community is run by the PebbleHive fmba association, which is a voluntary association.</p>
  <div class="price"><span class="price-cur">$</span><span class="price-val">250</span></div>
</article>

<article class="card" style="left:539px">
  <div class="card-photo" role="img" aria-label="Team working together around a table with a laptop" style="background:linear-gradient(160deg,#e8dccb 0%,#b89a7c 50%,#6b5646 100%)"></div>
  <h3 class="card-title">NEMO ENIM IPSAM</h3>
  <div class="card-rule"></div>
  <p class="card-text">The PebbleHive office community is run by the PebbleHive fmba association, which is a voluntary association.</p>
  <div class="price"><span class="price-cur">$</span><span class="price-val">250</span></div>
</article>

<div class="home-band"><div class="btn-outline">GO TO HOME PAGE</div></div>

<section class="contact" role="img" aria-label="Red-tinted group of community members behind contact details">
  <p class="cta-head">Do you need co-working space,<br>have a question or comment?</p>
  <div class="cta-btn">GET MORE INFO</div>
  <div class="divider"></div>

  <div class="col-head" style="left:382px">Visit us</div>
  <div class="info" style="top:81px">
    <svg width="8" height="10" viewBox="0 0 8 10"><path d="M4 0a4 4 0 0 0-4 4c0 3 4 6 4 6s4-3 4-6a4 4 0 0 0-4-4z" fill="#fff"/><circle cx="4" cy="4" r="1.4" fill="#b5161a"/></svg>
    <span>PebbleHive fmba, Mosegade 12<br>9000 Aalborg, Denmark</span></div>
  <div class="info" style="top:120px">
    <svg width="8" height="8" viewBox="0 0 8 8"><path d="M1.5 0l1.6 2-1 1.2a5 5 0 0 0 2.7 2.7l1.2-1L8 6.5 6.8 8C3 7.6.4 5 0 1.2z" fill="#fff"/></svg>
    <span>Call us: (+45) 20 11 47 30</span></div>
  <div class="info" style="top:143px">
    <svg width="9" height="7" viewBox="0 0 9 7"><rect width="9" height="7" fill="#fff"/><path d="M0 0l4.5 3.5L9 0" fill="none" stroke="#b5161a" stroke-width="1"/></svg>
    <span>Email us: info@pebblehive.dk</span></div>

  <div class="col-head" style="left:609px">Opening Hours</div>
  <p class="hours">For residents:&nbsp; 24-7, all weekdays.<br>For guests:&nbsp; 9: 00-16: 00,<br>Monday-Friday.</p>
</section>

<footer class="footer">
  <nav class="foot-nav"><span>Home</span><span class="sep">|</span><span>Residents</span><span class="sep">|</span><span>Our Working Space</span><span class="sep">|</span><span>Our Event Space</span><span class="sep">|</span><span>Contact Us</span></nav>
  <div class="foot-rule"></div>
  <p class="copyright">Copyright © 2018. PebbleHive. All rights reserved.</p>
  <div class="foot-brand">PEBBLEHIVE</div>
  <div class="social" aria-label="Social links"><span></span><span></span><span></span><span></span><span></span></div>
</footer>

</body>
</html>
```